Financial Consulting Company in need of technical diagram

Attached is a basic template to follow, however the following changes must be made:
- Get rid of reflection boxes at the bottom
-Delete anything in parentheses
-Change top box to read "Uncover Value Opportunities"
-Change bottom right box to read "Sales and Operations Planning"
-Change bottom left box to read "Financial Planning"

Additionally we would like to see something a little more creative and cohesive. One possibility is using "Cheveron" type arrows to show the "wheel" effect.

Please email tmorven@brightlake7.example if you have any questions!
Updates

Please see newly uploaded image for an example of how we would like it re-created.

Industry/Entity Type

Financial

Requirements
Must have
• I'm looking for something that keeps the "wheel" approach, but is not a direct re-creation of the example given. The boxes for example, dont' necessarily need to stay boxes. Feel free to play around with placement as well.
Nice to have
• Please see green wheel for example of how it can be re-created.

```html
<!DOCTYPE html>
<html lang="en">
<head>
<meta charset="utf-8">
<title>Value Cycle Diagram</title>
<link href="https://fonts.googleapis.com/css2?family=Roboto:wght@700&display=swap" rel="stylesheet">
<style>
  :root {
    --bg: #231f20;
    --blue-light: #4cc8f5;
    --blue: #1fb0ea;
    --blue-dark: #0a86bd;
    --text: #ffffff;
  }
  html, body {
    margin: 0;
    padding: 0;
    width: 1200px;
    height: 960px;
    overflow: hidden;
    background: var(--bg);
  }
  .diagram {
    position: relative;
    width: 1200px;
    height: 960px;
    background: var(--bg);
    font-family: "Roboto", "Helvetica Neue", Arial, sans-serif;
  }
  .cycle-arrows {
    position: absolute;
    inset: 0;
    filter: drop-shadow(3px 5px 4px rgba(0,0,0,0.55));
  }
  .arrow-shaft {
    fill: none;
    stroke: var(--blue);
    stroke-width: 20;
  }
  .arrow-head {
    fill: var(--blue);
  }
  .stage {
    position: absolute;
    width: 203px;
    height: 116px;
    box-sizing: border-box;
    border-radius: 18px;
    background: linear-gradient(180deg, var(--blue-light) 0%, var(--blue) 55%, var(--blue-dark) 100%);
    box-shadow: 0 6px 0 var(--blue-dark), 4px 10px 10px rgba(0,0,0,0.6);
    display: flex;
    align-items: center;
    justify-content: center;
    text-align: center;
    color: var(--text);
    font-weight: 700;
    font-size: 20px;
    line-height: 1.35;
    text-shadow: 0 1px 2px rgba(0,0,0,0.35);
  }
  .stage--uncover    { left: 497px; top: 97px; }
  .stage--strategize { left: 840px; top: 412px; }
  .stage--sales      { left: 672px; top: 737px; }
  .stage--financial  { left: 322px; top: 737px; }
  .stage--assess     { left: 157px; top: 403px; }
</style>
</head>
<body>
<main class="diagram">
  <svg class="cycle-arrows" width="1200" height="960" viewBox="0 0 1200 960" aria-hidden="true">
    <path class="arrow-shaft" d="M717 176 A343 343 0 0 1 897 327"/>
    <polygon class="arrow-head" points="918,315 876,339 918,370"/>

    <path class="arrow-shaft" d="M938 558 A343 343 0 0 1 888 685"/>
    <polygon class="arrow-head" points="908,698 868,672 863,719"/>

    <path class="arrow-shaft" d="M526 818 Q599 846 672 818"/>

    <path class="arrow-shaft" d="M337 718 A343 343 0 0 1 282 627"/>
    <polygon class="arrow-head" points="260,636 304,618 269,587"/>

    <path class="arrow-shaft" d="M278 381 A343 343 0 0 1 460 185"/>
    <polygon class="arrow-head" points="450,163 470,207 500,170"/>
  </svg>

  <div class="stage stage--uncover">Uncover Value<br>Opportunities</div>
  <div class="stage stage--strategize">Strategize<br>&amp;<br>Align</div>
  <div class="stage stage--sales">Sales Operations<br>Planning</div>
  <div class="stage stage--financial">Financial<br>Planning</div>
  <div class="stage stage--assess">Assess<br>the Results</div>
</main>
</body>
</html>
```